Maple Hound Web Site

We have basically a start up business that I need help with. This project is just for the web site.

Our product is a frozen raw pet food that promotes weight control, less shedding, smaller stools and an overall better health. The product is in nugget form similar to what you would see in a steak shish kabob. I only share that with you in case you want to incorporate that in the design.

We have been in business for 17 years but all of our sales have been word of mouth. We are going to be launching an infomercial this summer and I need everything stated previously to be completed before we can launch the infomercial.

We need the following (6) pages:

Home:
This is where we need to have the ability to purchase our products. Our main goal is to get the consumer to purchase our product. We have our own shopping cart so we just need to allow for the insertion of that shopping cart.

Why Raw:
This will just be a page with 4-5 paragraphs and an embedded YouTube video.

How to Use:
We will need a page with a chart (4 Columns wide with 6 rows) as well as an embedded YouTube video.

Customer Success Stories:
Allow us to add these as we move forward. I need a placeholder for an image of the customers pet and a paragraph or two explaining the situation

Where to Buy:
- Online - Find a Retailer - Find a Local Distributor - Call to Order

Contact Us:
Copper Ridge Holdings, Inc.
4217 Linden Wy
Eagan, MN 55122
(800) 555-0147

We need to provide links to our to be created... Facebook page, Twitter Account, Youtube Channel, Google circle, Blog
Updates

All, I have received many front page designs that look good.  Please notice in the brief that I need multiple pages built not just the home page.  

Thanks,

Todd

Reason: I need to see the rest of the pages. Thanks, Todd

Target Market(s)

Women between the ages of 30 & 60.

Industry/Entity Type

Shopping

```html
<!DOCTYPE html>
<html lang="en">
<head>
<meta charset="utf-8">
<title>Maple Hound — Natural Raw Dog Food</title>
<link href="https://fonts.googleapis.com/css2?family=Oswald:wght@400;500&family=Open+Sans:wght@400;600&display=swap" rel="stylesheet">
<style>
:root{
  --orange:#e0620c;
  --orange-light:#f08a2a;
  --orange-dark:#b94a06;
  --yellow:#f5c81e;
  --ink:#2b2b2b;
  --text:#444;
  --muted:#777;
  --pink:#fbe4e4;
  --line:#d6d6d6;
  --footer:#2f2f31;
  --footer-bottom:#232325;
  --footer-text:#b8b8b8;
}
*{box-sizing:border-box;margin:0;padding:0}
html,body{width:1200px;height:2211px;overflow:hidden}
body{position:relative;background:#fdf9f9;font-family:"Open Sans",Arial,sans-serif;color:var(--text)}
.abs{position:absolute}
.hero-bg{left:0;top:0;width:1200px;height:612px;background:radial-gradient(ellipse at 50% 40%,#f7f7f7 0%,#e6e6e6 60%,#cfcfcf 100%)}
.page-bg{left:0;top:612px;width:1200px;height:1281px;background:linear-gradient(#fbeaea,#fff 40%,#fff)}

.top-links{right:124px;top:24px;font:500 12px "Oswald",sans-serif;color:var(--orange-dark);letter-spacing:.3px}
.top-links span{margin:0 5px;color:#777}
.btn-pill{height:23px;border-radius:12px;font:12px "Open Sans",sans-serif;text-align:center;line-height:23px}
.sign-in{left:904px;top:65px;width:84px;background:linear-gradient(#f28a2c,var(--orange-dark));color:#fff}
.register{left:996px;top:65px;width:84px;background:linear-gradient(#ffe35a,#f0b800);color:#333}

.logo{left:121px;top:48px;display:flex;align-items:center;gap:12px}
.logo-mark{width:46px;height:46px;background:var(--orange)}
.logo-name{font:500 38px "Oswald",sans-serif;color:var(--ink);line-height:1}
.logo-tag{left:121px;top:114px;font:500 11px "Oswald",sans-serif;color:var(--ink);letter-spacing:1.5px}

.cart{left:622px;top:122px;display:flex;align-items:center;gap:10px;font:500 14px "Oswald",sans-serif;color:var(--orange-dark)}
.cart .items{margin-left:22px}
.search{left:865px;top:116px;width:214px;height:33px;border-radius:17px;background:#fff;border:1px solid #ddd;padding-left:16px;font:12px "Open Sans",sans-serif;line-height:31px;color:#555}
.search svg{position:absolute;right:12px;top:8px}

.nav{left:119px;top:172px;width:961px;height:46px;border-radius:5px;background:linear-gradient(#f39a3b,var(--orange) 55%,#c95208);display:flex;align-items:center;border:1px solid #c0540a}
.nav a{font:500 18px "Oswald",sans-serif;color:#fff;text-decoration:none;text-align:center;border-right:1px solid rgba(255,255,255,.35);height:30px;line-height:30px}
.nav a:last-child{border-right:none}

.slider{left:119px;top:240px;width:674px;height:326px;border-radius:12px;background:#d89a75}
.slide{left:134px;top:255px;width:646px;height:298px;background:linear-gradient(135deg,#5f8c2f,#c99a55 55%,#d9a862)}
.slide-caption{right:436px;top:436px;font:400 32px/42px "Oswald",sans-serif;color:#fff;text-align:right;text-shadow:0 2px 4px rgba(0,0,0,.5)}
.dots{left:412px;top:579px;display:flex;gap:8px}
.dots i{width:12px;height:12px;border-radius:50%;background:#fff;box-shadow:0 1px 2px rgba(0,0,0,.3)}
.dots i.on{background:var(--orange)}

.call-photo{left:815px;top:240px;width:265px;height:279px;background:linear-gradient(#e9e9e9,#cfcac6 60%,#2e2e2e)}
.call-btn{left:815px;top:519px;width:265px;height:47px;background:linear-gradient(#f08a2a,var(--orange-dark));border-radius:0 0 6px 6px;font:500 27px/47px "Oswald",sans-serif;color:#fff;text-align:center;letter-spacing:1px}

.live-chat{left:1148px;top:528px;width:52px;height:165px;background:#3a3a3a;border-radius:6px 0 0 6px}
.live-chat span{position:absolute;left:6px;top:112px;transform:rotate(-90deg);transform-origin:left top;font:500 24px "Oswald",sans-serif;color:#fff;white-space:nowrap}

.section-bar{left:119px;top:637px;width:961px;height:41px;border-radius:6px;background:linear-gradient(#f39a3b,var(--orange) 55%,#c95208)}
.section-bar h2{position:absolute;left:20px;top:0;font:500 19px/41px "Oswald",sans-serif;color:#fff}
.pager{position:absolute;right:12px;top:0;font:500 18px/41px "Oswald",sans-serif;color:#fff;display:flex;gap:14px;align-items:center}

.card{width:202px;height:250px;background:#fff;border:1px solid var(--line)}
.card .pack{position:absolute;left:48px;top:10px;width:104px;height:160px}
.card .meta{position:absolute;left:0;bottom:0;width:100%;height:71px;background:var(--pink);border-top:1px solid #eaa;padding:8px 0 0 19px}
.meta p{font:13px "Open Sans",sans-serif;color:#333}
.meta .price{position:absolute;left:19px;top:35px;font:500 17px "Oswald",sans-serif;color:#333}
.meta .add{position:absolute;left:77px;top:33px;width:107px;height:26px;background:var(--orange);border:1px solid var(--orange-dark);font:500 13px/24px "Oswald",sans-serif;color:#fff;padding-left:36px}
.meta .add svg{position:absolute;left:9px;top:5px}
.pack-dark{background:linear-gradient(#2a2a2a,#4a4a4a 60%,#3f7fc4)}
.pack-gold{background:linear-gradient(#c69a3a,#b08c45 60%,#4aa19b)}
.pack-blue{background:linear-gradient(#1f5aa8,#2a68b8)}

.view-more{left:943px;top:1282px;width:137px;height:39px;border-radius:5px;background:linear-gradient(#4a4a4a,#1f1f1f);font:16px/39px "Open Sans",sans-serif;color:#fff;text-align:center}

.videos{left:121px;top:1352px;width:959px;height:213px;background:#fff;border:1px solid #eee;box-shadow:0 2px 2px rgba(0,0,0,.06)}
.thumb{top:1366px;width:274px;height:186px;border:3px solid #ddd}
.thumb .play{position:absolute;left:50%;top:50%;width:40px;height:40px;margin:-20px 0 0 -20px;border-radius:50%;border:2px solid #fff;background:rgba(0,0,0,.35)}
.thumb .play::after{content:"";position:absolute;left:14px;top:10px;border-left:14px solid #fff;border-top:9px solid transparent;border-bottom:9px solid transparent}

.testimonial{left:121px;top:1599px;width:959px;height:251px;background:#fff;border:1px solid #eee;box-shadow:0 2px 2px rgba(0,0,0,.06)}
.testi-photo{left:125px;top:1604px;width:333px;height:240px;background:linear-gradient(90deg,#cfc6bb,#e9d9c8 50%,#b0734a)}
.quote{left:514px;top:1636px;width:545px;font:16px/24.5px "Open Sans",sans-serif;color:#333}
.qmark{font:500 48px "Oswald",sans-serif;color:var(--orange)}
.client{right:154px;top:1786px;font:500 17px "Oswald",sans-serif;color:#222}

.footer{left:0;top:1893px;width:1200px;height:275px;background:var(--footer)}
.footer-bottom{left:0;top:2168px;width:1200px;height:43px;background:var(--footer-bottom);font:11.5px/43px "Open Sans",sans-serif;color:#888}
.col{top:1924px;height:200px}
.col h3{font:400 20px "Oswald",sans-serif;color:#eee;margin-bottom:10px}
.col li{list-style:none;font:12.5px/24px "Open Sans",sans-serif;color:var(--footer-text)}
.col.sep{border-right:1px dashed #555}
.contact p{font:12.5px "Open Sans",sans-serif;color:var(--footer-text)}
.email{left:842px;top:2009px;width:236px;height:33px;background:#fff;border:1px solid #ccc;font:14px/31px "Open Sans",sans-serif;color:#aaa;padding-left:12px}
.subscribe{left:992px;top:2050px;width:86px;height:27px;background:var(--orange-dark);font:14px/27px "Open Sans",sans-serif;color:#fff;text-align:center}
.social{left:914px;top:2093px;display:flex;gap:9px}
.social i{width:26px;height:26px;border-radius:4px}
</style>
</head>
<body>
<div class="abs hero-bg"></div>
<div class="abs page-bg"></div>

<div class="abs top-links">MY ACCOUNT<span>/</span>WISH LIST<span>/</span>MY CART<span>/</span>CHECKOUT</div>
<div class="abs btn-pill sign-in">Sing in</div>
<div class="abs btn-pill register">Register</div>

<div class="abs logo"><div class="logo-mark"></div><div class="logo-name">Maple Hound</div></div>
<div class="abs logo-tag">100% NATURAL RAW DOG FOOD</div>

<div class="abs cart">
  <svg width="28" height="22" viewBox="0 0 28 22"><path d="M2 7h24l-3 13H5z" fill="#d66a1c"/><path d="M8 7l6-6 6 6" fill="none" stroke="#d66a1c" stroke-width="2"/></svg>
  SHOPPING CART<span class="items">(2) ITEMS</span>
</div>
<div class="abs search">Search.......
  <svg width="16" height="16" viewBox="0 0 16 16"><circle cx="6.5" cy="6.5" r="5" fill="none" stroke="#d2600c" stroke-width="2.2"/><path d="M10 10l5 5" stroke="#d2600c" stroke-width="2.4"/></svg>
</div>

<nav class="abs nav">
  <a style="width:78px"><svg width="22" height="18" viewBox="0 0 22 18" style="margin-top:6px"><path d="M11 1L1 10h3v7h5v-5h4v5h5v-7h3z" fill="#fff"/></svg></a>
  <a style="width:146px">Why Raw</a>
  <a style="width:171px">How to Use</a>
  <a style="width:192px">Where to Buy</a>
  <a style="width:213px">Success Stories</a>
  <a style="width:159px">Contact Us</a>
</nav>

<div class="abs slider"></div>
<div class="abs slide" role="img" aria-label="Three golden retriever puppies resting on a wooden plank in the grass"></div>
<div class="abs slide-caption">There are many variations of<br>passages of Lorem</div>
<div class="abs dots"><i></i><i></i><i class="on"></i><i></i><i></i></div>

<div class="abs call-photo" role="img" aria-label="Smiling customer service agent wearing a headset"></div>
<div class="abs call-btn">CALL NOW</div>

<div class="abs live-chat"><span>LIVE CHAT</span></div>

<div class="abs section-bar"><h2>Hot Products</h2>
  <div class="pager"><span>◂</span>1<span>2</span><span>3</span><span>▸</span></div>
</div>

<!-- product grid -->
<div class="abs card" style="left:121px;top:705px"><div class="pack pack-dark" role="img" aria-label="Bag of dry dog food"></div><div class="meta"><p>Literature from 45</p><div class="price">$ 323</div><div class="add"><svg width="18" height="14" viewBox="0 0 18 14"><path d="M1 5h16l-2 8H3z" fill="#fff"/><path d="M5 5l4-4 4 4" fill="none" stroke="#fff" stroke-width="1.5"/></svg>Add to Cart</div></div></div>
<div class="abs card" style="left:374px;top:705px"><div class="pack pack-dark" role="img" aria-label="Bag of dry dog food"></div><div class="meta"><p>Literature from 45</p><div class="price">$ 323</div><div class="add"><svg width="18" height="14" viewBox="0 0 18 14"><path d="M1 5h16l-2 8H3z" fill="#fff"/><path d="M5 5l4-4 4 4" fill="none" stroke="#fff" stroke-width="1.5"/></svg>Add to Cart</div></div></div>
<div class="abs card" style="left:628px;top:705px"><div class="pack pack-gold" role="img" aria-label="Bag of dry dog food"></div><div class="meta"><p>Literature from 45</p><div class="price">$ 323</div><div class="add"><svg width="18" height="14" viewBox="0 0 18 14"><path d="M1 5h16l-2 8H3z" fill="#fff"/><path d="M5 5l4-4 4 4" fill="none" stroke="#fff" stroke-width="1.5"/></svg>Add to Cart</div></div></div>
<div class="abs card" style="left:877px;top:705px"><div class="pack pack-blue" role="img" aria-label="Bag of dry dog food"></div><div class="meta"><p>Literature from 45</p><div class="price">$ 323</div><div class="add"><svg width="18" height="14" viewBox="0 0 18 14"><path d="M1 5h16l-2 8H3z" fill="#fff"/><path d="M5 5l4-4 4 4" fill="none" stroke="#fff" stroke-width="1.5"/></svg>Add to Cart</div></div></div>

<div class="abs card" style="left:121px;top:1001px"><div class="pack pack-dark" role="img" aria-label="Bag of dry dog food"></div><div class="meta"><p>Literature from 45</p><div class="price">$ 323</div><div class="add"><svg width="18" height="14" viewBox="0 0 18 14"><path d="M1 5h16l-2 8H3z" fill="#fff"/><path d="M5 5l4-4 4 4" fill="none" stroke="#fff" stroke-width="1.5"/></svg>Add to Cart</div></div></div>
<div class="abs card" style="left:374px;top:1001px"><div class="pack pack-dark" role="img" aria-label="Bag of dry dog food"></div><div class="meta"><p>Literature from 45</p><div class="price">$ 323</div><div class="add"><svg width="18" height="14" viewBox="0 0 18 14"><path d="M1 5h16l-2 8H3z" fill="#fff"/><path d="M5 5l4-4 4 4" fill="none" stroke="#fff" stroke-width="1.5"/></svg>Add to Cart</div></div></div>
<div class="abs card" style="left:628px;top:1001px"><div class="pack pack-gold" role="img" aria-label="Bag of dry dog food"></div><div class="meta"><p>Literature from 45</p><div class="price">$ 323</div><div class="add"><svg width="18" height="14" viewBox="0 0 18 14"><path d="M1 5h16l-2 8H3z" fill="#fff"/><path d="M5 5l4-4 4 4" fill="none" stroke="#fff" stroke-width="1.5"/></svg>Add to Cart</div></div></div>
<div class="abs card" style="left:877px;top:1001px"><div class="pack pack-blue" role="img" aria-label="Bag of dry dog food"></div><div class="meta"><p>Literature from 45</p><div class="price">$ 323</div><div class="add"><svg width="18" height="14" viewBox="0 0 18 14"><path d="M1 5h16l-2 8H3z" fill="#fff"/><path d="M5 5l4-4 4 4" fill="none" stroke="#fff" stroke-width="1.5"/></svg>Add to Cart</div></div></div>

<div class="abs view-more">View More »</div>

<div class="abs videos"></div>
<svg class="abs" style="left:134px;top:1446px" width="16" height="24" viewBox="0 0 16 24"><path d="M15 1L2 12l13 11z" fill="var(--orange)"/></svg>
<svg class="abs" style="left:1052px;top:1446px" width="16" height="24" viewBox="0 0 16 24"><path d="M1 1l13 11L1 23z" fill="var(--orange)"/></svg>
<div class="abs thumb" style="left:165px;background:linear-gradient(#6f8f4a,#4d7a2b)" role="img" aria-label="Video thumbnail: bulldog and puppy playing on grass"><div class="play"></div></div>
<div class="abs thumb" style="left:466px;background:linear-gradient(#7a8a55,#3f6a25)" role="img" aria-label="Video thumbnail: toddler sitting on grass beside puppies eating"><div class="play"></div></div>
<div class="abs thumb" style="left:765px;background:linear-gradient(135deg,#8a97a8,#8a5a35 60%,#9a9a9a)" role="img" aria-label="Video thumbnail: dog eating from a food bowl"><div class="play"></div></div>

<div class="abs testimonial"></div>
<div class="abs testi-photo" role="img" aria-label="Happy customer holding her small long-haired dog"></div>
<div class="abs" style="left:476px;top:1608px"><span class="qmark">“</span></div>
<p class="abs quote">Lorem ipsum dolor sit amet, consectetur adipiscing elit. Nulla ornare, nisi ut interdum condimentum, felis lectus pharetra nunc, nec tristique quam mi eu nunc. Nulla ornare sagittis ante, id sollicitudin nunc. Vestibulum ut sodales nisi. Pellentesque nunc dolor, faucibus in erat a, hendrerit mattis elit. Duis ornare mi ut risus egestas malesuada. <span class="qmark" style="font-size:44px;line-height:10px;vertical-align:-14px">”</span></p>
<div class="abs client">– Client Name Here</div>

<footer class="abs footer"></footer>
<div class="abs col sep" style="left:119px;width:126px"><h3>Quick Links</h3><ul><li>Why Raw</li><li>How to Use</li><li>Where to Buy</li><li>Success Stories</li><li>How to Use</li><li>Where to Buy</li><li>Contact Us</li></ul></div>
<div class="abs col sep" style="left:273px;width:126px"><h3>Top Products</h3><ul><li>Product 1</li><li>Product 2</li><li>Product 3</li><li>Product 4</li><li>Product 5</li><li>Product 6</li><li>Product 7</li></ul></div>
<div class="abs col sep" style="left:427px;width:156px"><h3>Where to Buy</h3><ul><li>Find a Retailer</li><li>Find a Local Distributor</li><li>Call to Order</li></ul></div>
<div class="abs col sep contact" style="left:615px;width:199px"><h3>Contact Information</h3>
  <p style="font-size:13px;margin-bottom:6px">PUBLISHING PACKAGES</p>
  <p style="font-size:11px;line-height:19px">Lorem Ipsum is therefore always free<br>from repetition</p>
  <p style="margin-top:8px;display:flex;gap:8px;align-items:center"><svg width="16" height="16" viewBox="0 0 16 16"><path d="M3 1l3 3-2 2c1 2 3 4 5 5l2-2 3 3-2 3C7 15 1 9 1 3z" fill="#ddd"/></svg>+0 (000) 000-0000</p>
</div>
<div class="abs col contact" style="left:840px;width:240px"><h3>Newsletter</h3><p style="font-size:12px;line-height:18px">combined with a handful of model<br>sentence structures.</p></div>
<div class="abs email">Email address</div>
<div class="abs subscribe">Subscribe</div>
<div class="abs social" aria-label="Social links"><i style="background:#3b62b5"></i><i style="background:#3f8ab8"></i><i style="background:#f09a1c"></i><i style="background:#d2382c"></i><i style="background:#b5322a"></i></div>

<div class="abs footer-bottom"><span style="position:absolute;left:121px">Company Name © 2014. Privacy Policy</span></div>
</body>
</html>
```